Author and Publisher

Cover for a book on the process of publishing a book from the presentation to the publisher until the selling in bookstores :
A behind-the-scenes journey through the world of book publishing, from manuscript to bookstore. The book explores the relationship between authors and publishers, manuscript selection, contracts, editing, proofreading, book design, printing, distribution, bookstores and online sales. It reveals the many people, decisions and processes involved in turning a text into a physical book and bringing it to readers. The illustration should evoke publishing as a lively, contemporary ecosystem, combining creativity, craftsmanship, business and the enduring appeal of books.
FORMAT : 14 x 20,5 cm
AUTHOR : Luc Varennes
TITLE : Le scribe et la presse
PUBLISHER : Editions Trovel (at the bottom of the page)
Target Market(s)
General public, mainly news authors of books
Look and feel
Each slider illustrates characteristics of the customer's brand and the style your logo design should communicate.

```html
<!DOCTYPE html>
<html lang="fr">
<head>
<meta charset="utf-8">
<title>Le scribe et la presse — Luc Varennes</title>
<link rel="stylesheet" href="https://fonts.googleapis.com/css2?family=Playfair+Display:wght@700;900&family=Montserrat:wght@500;600;700&family=Great+Vibes&display=swap">
<style>
  :root {
    --navy: #0d1c4a;
    --orange: #e8900f;
    --brown: #4a3512;
    --stage: #e3e3e3;
    --paper-top: #ffffff;
    --paper-bottom: #e9d9bd;
    --red: #c8161d;
    --green: #3fae7f;
    --tangerine: #f07a2a;
    --violet: #6b57b8;
    --print: #e8a21e;
    --warehouse: #2f6a52;
    --shelves: #4a3a2a;
  }
  * { box-sizing: border-box; margin: 0; padding: 0; }
  html, body { width: 891px; height: 1200px; overflow: hidden; background: var(--stage); }
  .cover {
    position: absolute; left: 36px; top: 0; width: 818px; height: 1200px;
    background: linear-gradient(180deg, var(--paper-top) 0%, var(--paper-top) 40%, var(--paper-bottom) 100%);
    overflow: hidden;
  }
  .title {
    position: absolute; left: 0; width: 100%; text-align: center;
    font-family: "Playfair Display", serif; font-weight: 700; color: var(--navy);
    font-size: 84px; line-height: 1; letter-spacing: 1px;
  }
  .title--first { top: 48px; }
  .title--second { top: 148px; }
  .title-rule { position: absolute; top: 143px; height: 1px; background: var(--orange); }
  .title-rule--left { left: 179px; width: 190px; }
  .title-rule--right { left: 448px; width: 190px; }
  .title-joiner {
    position: absolute; top: 108px; left: 0; width: 100%; text-align: center;
    font-family: "Great Vibes", cursive; color: var(--orange); font-size: 62px; line-height: 1;
  }
  .wheel { position: absolute; left: 0; top: 0; }
  .step {
    position: absolute; transform: translateX(-50%); text-align: center;
    font-family: "Montserrat", sans-serif; font-weight: 700; color: var(--navy);
    font-size: 13.5px; line-height: 16px; white-space: nowrap;
  }
  .author-rule { position: absolute; top: 1069px; height: 1px; background: var(--navy); }
  .author-rule--left { left: 64px; width: 134px; }
  .author-rule--right { left: 620px; width: 134px; }
  .author {
    position: absolute; top: 1046px; left: 0; width: 100%; text-align: center;
    font-family: "Montserrat", sans-serif; font-weight: 600; color: var(--navy);
    font-size: 44px; line-height: 48px; letter-spacing: 7px;
  }
  .publisher {
    position: absolute; top: 1112px; left: 0; width: 100%; text-align: center;
    font-family: "Montserrat", sans-serif; font-weight: 600; color: var(--brown);
    font-size: 20px; letter-spacing: 0.5px;
  }
</style>
</head>
<body>
<main class="cover">
  <h1>
    <span class="title title--first">LE SCRIBE</span>
    <span class="title-rule title-rule--left"></span>
    <span class="title-rule title-rule--right"></span>
    <span class="title-joiner">Et</span>
    <span class="title title--second">LA PRESSE</span>
  </h1>

  <svg class="wheel" width="818" height="1200" viewBox="0 0 818 1200">
    <defs>
      <radialGradient id="pagesTone" cx="361" cy="576" r="290" gradientUnits="userSpaceOnUse">
        <stop offset="0" stop-color="#b9bab6"/>
        <stop offset="0.45" stop-color="#e2e2e0"/>
        <stop offset="1" stop-color="#f7f7f6"/>
      </radialGradient>
      <filter id="bookShadow" x="-20%" y="-20%" width="140%" height="140%">
        <feDropShadow dx="0" dy="6" stdDeviation="8" flood-color="#000" flood-opacity="0.22"/>
      </filter>
    </defs>
    <g class="wedges">
      <path role="img" aria-label="Manuscrit sur une table rouge avec une tasse" fill="var(--red)" d="M361 576 L625 388 A336 336 0 0 1 704 489 Z"/>
      <path role="img" aria-label="Mains signant un contrat" fill="var(--green)" d="M361 576 L704 489 A336 336 0 0 1 741 659 Z"/>
      <path role="img" aria-label="Stylo rouge corrigeant un texte imprimé" fill="var(--tangerine)" d="M361 576 L741 659 A336 336 0 0 1 670 849 Z"/>
      <path role="img" aria-label="Écran de graphiste et nuanciers de couleurs" fill="var(--violet)" d="M361 576 L670 849 A336 336 0 0 1 481 969 Z"/>
      <path role="img" aria-label="Feuilles d'imprimerie colorées" fill="var(--print)" d="M361 576 L481 969 A336 336 0 0 1 263 946 Z"/>
      <path role="img" aria-label="Entrepôt de distribution avec rayonnages" fill="var(--warehouse)" d="M361 576 L263 946 A336 336 0 0 1 144 853 Z"/>
      <path role="img" aria-label="Rayons de librairie" fill="var(--shelves)" d="M361 576 L144 853 A336 336 0 0 1 89 757 Z"/>
    </g>
    <path class="book" role="img" aria-label="Livre ouvert aux pages déployées en éventail" fill="url(#pagesTone)" filter="url(#bookShadow)"
          d="M361 576 L563 368 A290 290 0 1 0 190 811 Z"/>

    <path class="ring" fill="none" stroke="var(--orange)" stroke-width="1.2" d="M618 369 A346 346 0 1 1 71 732"/>
    <g class="leaders" fill="none" stroke="var(--orange)" stroke-width="1">
      <polyline points="658,419 670,395 680,395"/>
      <polyline points="730,541 741,540 748,520"/>
      <polyline points="711,787 722,788 733,805"/>
      <polyline points="583,926 598,947 612,947"/>
      <polyline points="400,983 390,1001 375,1001"/>
      <polyline points="208,937 198,940 180,940"/>
      <polyline points="134,862 120,867 108,867"/>
    </g>
    <g class="icons" fill="none" stroke="var(--navy)" stroke-width="1.8" stroke-linejoin="round" stroke-linecap="round">
      <g transform="translate(693 346)"><path d="M2 2 H14 L20 8 V30 H2 Z M14 2 V8 H20"/><path d="M6 14 H16 M6 19 H16 M6 24 H12"/></g>
      <g transform="translate(734 458)"><path d="M2 4 L9 3 L15 8 L22 4 L30 6 V18 L26 18 L19 24 L12 18 L2 18 Z"/><path d="M15 8 L11 12 L14 14 L19 10 L24 15"/></g>
      <g transform="translate(745 780)"><path d="M22 2 L28 8 L10 26 L3 28 L5 21 Z M18 6 L24 12"/></g>
      <g transform="translate(633 914)"><path d="M16 3 C6 3 2 11 3 18 C4 26 12 30 17 27 C20 25 16 22 19 20 C22 18 28 20 29 14 C30 7 24 3 16 3 Z"/><circle cx="10" cy="12" r="2"/><circle cx="16" cy="9" r="2"/><circle cx="9" cy="19" r="2"/><path d="M20 22 L32 8"/></g>
      <g transform="translate(323 990)"><rect x="7" y="2" width="20" height="9" rx="2"/><rect x="2" y="11" width="30" height="14" rx="3"/><rect x="9" y="19" width="16" height="12"/><path d="M13 24 H21 M13 28 H19"/></g>
      <g transform="translate(104 894)"><path d="M2 4 C8 2 14 3 18 7 C22 3 28 2 34 4 V28 C28 26 22 27 18 30 C14 27 8 26 2 28 Z M18 7 V30"/></g>
      <g transform="translate(40 802)"><path d="M2 3 H8 L12 22 H32 L36 9 H10"/><path d="M15 9 L17 22 M22 9 V22 M29 9 L27 22 M11 15 H34"/><circle cx="15" cy="28" r="2.5"/><circle cx="28" cy="28" r="2.5"/></g>
    </g>
  </svg>

  <p class="step" style="left:727px; top:378px">Manuscrit</p>
  <p class="step" style="left:761px; top:484px">Contract<br>&amp; selectie</p>
  <p class="step" style="left:747px; top:808px">Redactie &amp;<br>correctie</p>
  <p class="step" style="left:663px; top:951px">Grafisch<br>ontwerp</p>
  <p class="step" style="left:349px; top:1026px">Indruk</p>
  <p class="step" style="left:137px; top:926px">Verdeling</p>
  <p class="step" style="left:70px; top:833px">Librairies a<br>ventes en<br>ligne</p>

  <span class="author-rule author-rule--left"></span>
  <p class="author">LUC VARENNES</p>
  <span class="author-rule author-rule--right"></span>
  <p class="publisher">PUBLISHER : EDITIONS TROVEL</p>
</main>
</body>
</html>
```